Upgrade your eyecare

Print advertisement (newspaper, magazine). Add for optometry office and optical boutique "Harwellton Optic Group." We provide eye exams and eyewear with cutting edge technology and are located in a tech-savy college town. We would like the add to mimic an quorel (or zelpad?) screen for app update/upgrades. We want to attract new customers / patients who are tech savy and would appreciate a high-tech medical office. Something like: 'Eyecare and eye wear app' uprade available, with some graphics like swipe to upgrade, etc. See www.harwelltonoptic.com for some of our color schemes and graphics

Reason: I apologize if the brief was unclear. I am looking for something to print in newspaper and magazines, size about 6"x6". The idea is that your eyes deserve the best technology, so I wanted to tie into the smartphone generation by using zelpad or quorel imagery about an upgrade is available. It could be someone holding a phone with some text/logos, it could be more abstract. There are some great ideas, but I feel some people may want/need a few more days to fine tune submissions, so I'm extending it a few days. Thanks everyone! Please ask any questions.

```html
<!DOCTYPE html>
<html lang="en">
<head>
<meta charset="utf-8">
<title>Harwellton Optic Group — Eyecare and Eye Wear</title>
<link rel="stylesheet" href="https://fonts.googleapis.com/css2?family=Share+Tech+Mono&family=Dancing+Script:wght@700&display=swap">
<style>
  :root {
    --backdrop: #f4f2f4;
    --plum-deep: #6a1f5e;
    --plum: #8a3a7c;
    --mauve: #c48db8;
    --mauve-light: #d9b4cf;
    --ink-plum: #7a2a6c;
    --ink-dark: #4a3a46;
    --photo-light: #e6e6e6;
    --photo-mid: #a9a9a9;
    --white: #ffffff;
    --phone-silver: #e9e9ec;
    --phone-edge: #c9c9cf;
  }
  * { box-sizing: border-box; margin: 0; padding: 0; }
  html, body { width: 1200px; height: 900px; overflow: hidden; background: var(--backdrop); }
  body { font-family: "Share Tech Mono", monospace; }

  .flyer {
    position: absolute; left: 350px; top: 60px;
    width: 500px; height: 780px; overflow: hidden;
    background: linear-gradient(160deg, var(--plum) 0%, var(--plum-deep) 55%, #5c1752 100%);
    box-shadow: 0 6px 24px rgba(0,0,0,.18);
  }

  .eye-photo {
    position: absolute; left: 230px; top: 0; width: 270px; height: 700px;
    background: radial-gradient(ellipse at 45% 40%, var(--photo-mid) 0%, var(--photo-light) 45%, #f1f1f1 100%);
    clip-path: polygon(22% 0, 100% 0, 100% 100%, 4% 100%, 6% 70%, 0 52%, 8% 40%, 16% 18%);
  }

  .brand { position: absolute; left: 36px; top: 42px; display: flex; align-items: center; gap: 10px; }
  .brand-square { width: 40px; height: 40px; background: var(--mauve-light); border-radius: 4px; }
  .brand-name { color: var(--white); font-size: 17px; line-height: 1.1; width: 140px; }

  .contact {
    position: absolute; right: 30px; top: 60px; text-align: right; font-style: normal;
    color: var(--ink-plum); font-size: 11px; line-height: 1.6; letter-spacing: .5px;
  }

  .headline-card {
    position: absolute; left: 36px; top: 165px; width: 192px; height: 215px;
    border: 6px solid var(--white); border-radius: 20px;
    background: linear-gradient(180deg, var(--mauve-light), var(--mauve));
    text-align: center; color: var(--ink-plum);
    display: flex; flex-direction: column; justify-content: center; align-items: center;
  }
  .dot-row { display: flex; gap: 6px; margin: 6px 0; }
  .dot-row span { width: 4px; height: 4px; border-radius: 50%; background: var(--white); }
  .headline-card .big { font-size: 34px; line-height: 1.1; }
  .headline-card .script { font-family: "Dancing Script", cursive; font-size: 30px; color: var(--white); line-height: 1.1; }

  .phone {
    position: absolute; left: 34px; top: 400px; width: 204px; height: 420px;
    background: var(--phone-silver); border: 2px solid var(--phone-edge); border-radius: 30px;
  }
  .phone-speaker { position: absolute; left: 82px; top: 24px; width: 38px; height: 5px; border-radius: 3px; background: #9a9aa0; }
  .phone-camera { position: absolute; left: 97px; top: 10px; width: 7px; height: 7px; border-radius: 50%; background: #9a9aa0; }
  .phone-screen {
    position: absolute; left: 12px; top: 62px; width: 176px; height: 360px;
    background: linear-gradient(180deg, var(--mauve-light), var(--mauve)); overflow: hidden;
  }
  .status-bar { height: 14px; background: #111; color: var(--white); font-size: 8px; padding: 2px 6px; }
  .app-title { text-align: center; color: var(--ink-dark); margin-top: 18px; }
  .app-title .big { font-size: 30px; line-height: 1.05; }
  .app-title .script { font-family: "Dancing Script", cursive; color: var(--ink-plum); font-size: 20px; line-height: .9; }
  .eye-icon { display: block; margin: 12px auto 0; }
  .upgrade-button {
    position: absolute; left: 14px; top: 262px; width: 148px; height: 30px;
    background: rgba(106,31,94,.55); border-radius: 4px; display: flex; align-items: center;
    color: var(--white); font-size: 9px; letter-spacing: 1px;
  }
  .upgrade-button .arrow-box { width: 30px; height: 30px; background: var(--plum-deep); border-radius: 4px 0 0 4px; display: flex; align-items: center; justify-content: center; margin-right: 16px; }

  .benefits {
    position: absolute; left: 285px; top: 548px; width: 190px;
    color: #8e8e8e; font-size: 9.5px; line-height: 1.5; text-transform: uppercase; list-style: none;
  }
  .benefits li::before { content: "•"; margin-right: 6px; }

  .footer-band { position: absolute; left: 0; top: 700px; width: 500px; height: 80px; background: var(--white); }
  .footer-dots { position: absolute; left: 256px; top: 727px; display: flex; gap: 9px; }
  .footer-dots span { width: 5px; height: 5px; border-radius: 50%; background: var(--mauve); }
  .web { position: absolute; right: 30px; top: 720px; color: var(--ink-plum); font-size: 10px; letter-spacing: .5px; }
</style>
</head>
<body>
  <main class="flyer">
    <div class="eye-photo" role="img" aria-label="Black and white close-up photo of a woman's eye and lashes"></div>

    <div class="brand">
      <div class="brand-square"></div>
      <div class="brand-name">Harwellton Optic Group</div>
    </div>

    <address class="contact">
      PHONE: (555)014-7380<br>2870 LINDEN CREST AVENUE<br>HARWELLTON
    </address>

    <section class="headline-card">
      <div class="dot-row"><span></span><span></span><span></span><span></span><span></span></div>
      <div class="big">EYECARE</div>
      <div class="script">and</div>
      <div class="big">EYE WEAR</div>
      <div class="dot-row"><span></span><span></span><span></span><span></span><span></span></div>
    </section>

    <ul class="benefits">
      <li>Digital eye exams with same day results</li>
      <li>Designer frames fitted in our boutique</li>
      <li>Contact lens fittings for every lifestyle</li>
      <li>Evening hours for busy students</li>
    </ul>

    <div class="footer-band"></div>
    <div class="footer-dots"><span></span><span></span><span></span><span></span><span></span></div>
    <div class="web">WWW.HARWELLTONOPTIC.COM</div>

    <div class="phone">
      <div class="phone-camera"></div>
      <div class="phone-speaker"></div>
      <div class="phone-screen">
        <div class="status-bar">.ıll CARRIER</div>
        <div class="app-title">
          <div class="big">TIME</div>
          <div class="script">to</div>
          <div class="big">UPGRADE</div>
          <div class="script">your</div>
          <div class="big">EYE CARE</div>
        </div>
        <svg class="eye-icon" width="150" height="34" viewBox="0 0 150 34" aria-hidden="true">
          <g fill="#6a1f5e">
            <circle cx="8" cy="17" r="1.6"/><circle cx="16" cy="17" r="1.6"/><circle cx="24" cy="17" r="1.6"/><circle cx="32" cy="17" r="1.6"/>
            <circle cx="118" cy="17" r="1.6"/><circle cx="126" cy="17" r="1.6"/><circle cx="134" cy="17" r="1.6"/><circle cx="142" cy="17" r="1.6"/>
          </g>
          <path d="M47 17 Q75 -4 103 17 Q75 38 47 17 Z" fill="none" stroke="#6a1f5e" stroke-width="3"/>
          <circle cx="75" cy="17" r="9" fill="#6a1f5e"/>
          <circle cx="75" cy="17" r="4" fill="#d9b4cf"/>
        </svg>
        <div class="upgrade-button">
          <span class="arrow-box">
            <svg width="16" height="12" viewBox="0 0 16 12" aria-hidden="true"><path d="M0 4h9V0l7 6-7 6V8H0z" fill="#fff"/></svg>
          </span>
          UPGRADE NOW
        </div>
      </div>
    </div>
  </main>
</body>
</html>
```